Women's Online Clothing Boutique Needs Business Cards

I already have a logo that I would like to use. Some of the things that interest me is black business cards, foil embossed logo, glossy embossed logo, leopard print, no yellow font, rounded edges. I even like just a large logo on the front side with all of my information on the back side.

Contact Information for Business Card

https://copperfinch.shopvendly.example/
https://www.facebook.com/thecopperfinchboutique/
https://www.instagram.com/thecopperfinchboutique/
copperfinchboutique@mailora.example

Requirements
Must have
• My Logo
Nice to have
• Leopard Print
Should not have
• No Yellow Font

```html
<!DOCTYPE html>
<html lang="en">
<head>
<meta charset="utf-8">
<title>The Copper Finch Boutique – Business Cards</title>
<link href="https://fonts.googleapis.com/css2?family=Roboto:wght@300;400&display=swap" rel="stylesheet">
<style>
  :root {
    --stage: #1c1c1c;
    --card-black: #1f1f21;
    --card-white: #ffffff;
    --gold: #c9a043;
    --emboss: #4a4a4d;
    --ink: #333333;
  }
  html, body {
    margin: 0;
    padding: 0;
    width: 1200px;
    height: 930px;
    overflow: hidden;
    background: var(--stage);
    font-family: 'Roboto', Arial, sans-serif;
  }
  .canvas {
    position: relative;
    width: 1200px;
    height: 930px;
  }
  .card {
    position: absolute;
    left: 290px;
    width: 620px;
    height: 354px;
    border-radius: 22px;
    box-sizing: border-box;
  }
  .card--front {
    top: 92px;
    background: linear-gradient(135deg, #2a2a2c 0%, var(--card-black) 55%, #18181a 100%);
  }
  .card--back {
    top: 484px;
    background: var(--card-white);
  }
  .brand {
    position: absolute;
    left: 0;
    right: 0;
    text-align: center;
    font-weight: 300;
    letter-spacing: 0.5px;
    line-height: 1.15;
  }
  .card--front .brand {
    top: 120px;
    font-size: 38px;
    color: var(--emboss);
  }
  .card--back .brand {
    top: 52px;
    font-size: 30px;
    color: var(--gold);
  }
  .brand__rule {
    display: block;
    width: 250px;
    height: 1px;
    margin: 10px auto 0;
    background: currentColor;
  }
  .divider {
    position: absolute;
    left: 40px;
    right: 40px;
    top: 190px;
    height: 1px;
    background: var(--gold);
  }
  .contact {
    position: absolute;
    list-style: none;
    margin: 0;
    padding: 0;
    font-size: 15px;
    color: var(--ink);
  }
  .contact li {
    display: flex;
    align-items: center;
    gap: 9px;
    height: 26px;
  }
  .contact--web {
    right: 30px;
    top: 208px;
    text-align: right;
  }
  .contact--web li { justify-content: flex-end; }
  .contact--social {
    left: 30px;
    bottom: 26px;
  }
  .icon {
    width: 17px;
    height: 17px;
    flex: none;
  }
</style>
</head>
<body>
<div class="canvas">

  <section class="card card--front" aria-label="Card front">
    <div class="brand">The Copper Finch Boutique<span class="brand__rule"></span></div>
  </section>

  <section class="card card--back" aria-label="Card back">
    <div class="brand">The Copper Finch Boutique<span class="brand__rule"></span></div>

    <div class="divider"></div>

    <ul class="contact contact--web">
      <li>copperfinchboutique@mailora.example
        <svg class="icon" viewBox="0 0 20 20" aria-hidden="true">
          <circle cx="10" cy="10" r="10" fill="var(--gold)"/>
          <rect x="5" y="6.5" width="10" height="7" fill="none" stroke="#fff" stroke-width="1.3"/>
          <path d="M5 6.5 L10 10.5 L15 6.5" fill="none" stroke="#fff" stroke-width="1.3"/>
        </svg>
      </li>
      <li>copperfinch.shopvendly.example
        <svg class="icon" viewBox="0 0 20 20" aria-hidden="true">
          <circle cx="10" cy="10" r="10" fill="var(--gold)"/>
          <circle cx="10" cy="10" r="5.5" fill="none" stroke="#fff" stroke-width="1.2"/>
          <ellipse cx="10" cy="10" rx="2.3" ry="5.5" fill="none" stroke="#fff" stroke-width="1.1"/>
          <path d="M4.5 10 H15.5" stroke="#fff" stroke-width="1.1"/>
        </svg>
      </li>
    </ul>

    <ul class="contact contact--social">
      <li>
        <svg class="icon" viewBox="0 0 20 20" aria-hidden="true"><circle cx="10" cy="10" r="10" fill="var(--gold)"/></svg>
        thecopperfinchboutique/
      </li>
      <li>
        <svg class="icon" viewBox="0 0 20 20" aria-hidden="true"><circle cx="10" cy="10" r="10" fill="var(--gold)"/></svg>
        thecopperfinchboutique/
      </li>
    </ul>
  </section>

</div>
</body>
</html>
```